Verpackungsdesign für Lifestyle-Diagnostik und Supplements im Bereich Longevity
Zielgruppe
Wir machen Lifestyle-Diagnostik und Supplements im Bereich Longevity
Aufgabenstellung
Verpackung eines Tests (wie der hier: https://shop.quellmora.com/products/zentrip) in der gezeigten Metallschachtel, Supplements in den gezeigten Dosen. Ein Set besteht aus einem Test und zwei Dosen (morgens und abends). Farbschema und Logo Korunelle wie im Anhang. paar Details zu den Supplements auch in den Dateien
Bitte auch an Prägung und anderen Gestaltungsmöglichkeiten denken

```html
<!DOCTYPE html>
<html lang="de">
<head>
<meta charset="utf-8">
<title>Korunelle – Longevity Set Etiketten</title>
<link rel="stylesheet" href="https://fonts.googleapis.com/css2?family=Arimo:wght@400;700&family=Barlow+Condensed:ital,wght@0,600;1,300;1,400&display=swap">
<style>
  :root {
    --teal: #0f4a50;
    --green: #9cc23a;
    --green-light: #d3e88c;
    --green-pale: #e8f3c4;
    --ink: #2f3a3c;
    --muted: #5d6668;
    --canvas: #efefed;
    --paper: #ffffff;
  }
  html, body {
    margin: 0;
    padding: 0;
    width: 1200px;
    height: 2258px;
    overflow: hidden;
    background: var(--canvas);
  }
  .sheet {
    position: relative;
    width: 1200px;
    height: 2258px;
  }
  .label {
    position: absolute;
    display: block;
    background: var(--paper);
    box-shadow: 0 6px 22px rgba(0,0,0,0.12);
  }
  .label--am   { left: 50px;  top: 120px; width: 540px; height: 688px; }
  .label--pm   { left: 610px; top: 120px; width: 540px; height: 688px; }
  .label--test { left: 200px; top: 888px; width: 800px; height: 1181px; }

  .brand-name { font-family: "Arimo", Arial, sans-serif; font-weight: 700; fill: var(--teal); }
  .headline { font-family: "Barlow Condensed", "Arial Narrow", sans-serif; font-weight: 600; }
  .hl-green { fill: var(--green); }
  .hl-teal { fill: var(--teal); }
  .body-text { font-family: "Arimo", Arial, sans-serif; fill: var(--ink); }
  .muted-text { font-family: "Arimo", Arial, sans-serif; fill: var(--muted); }
  .white-text { font-family: "Arimo", Arial, sans-serif; fill: #fff; }
  .strong { font-weight: 700; }
  .percent { font-family: "Barlow Condensed", "Arial Narrow", sans-serif; font-style: italic; font-weight: 300; fill: var(--green); }
  .count { font-family: "Barlow Condensed", "Arial Narrow", sans-serif; font-weight: 600; fill: var(--green); }
  .dose-count { font-family: "Barlow Condensed", "Arial Narrow", sans-serif; font-weight: 400; fill: var(--green-pale); }
</style>
</head>
<body>
<main class="sheet">

  <!-- AM Formel tin label -->
  <svg class="label label--am" viewBox="0 0 383 488" aria-labelledby="am-title">
    <title id="am-title">Korunelle AM Formel Etikett</title>
    <defs>
      <linearGradient id="am-pill" x1="0" y1="0" x2="0" y2="1">
        <stop offset="0" stop-color="#d9ec9a"/>
        <stop offset="1" stop-color="#9cc23a"/>
      </linearGradient>
      <linearGradient id="am-panel" x1="0" y1="0" x2="1" y2="1">
        <stop offset="0" stop-color="#b5d55a"/>
        <stop offset="1" stop-color="#97bf33"/>
      </linearGradient>
    </defs>

    <g class="time-pill">
      <path d="M296 0 H336 V250 A20 20 0 0 1 296 250 Z" fill="url(#am-pill)"/>
      <text class="white-text" font-size="13" transform="translate(321 200) rotate(-90)">Morgens einnehmen</text>
      <g class="icon-sun" stroke="#fff" stroke-width="1.6" stroke-linecap="round">
        <circle cx="316" cy="243" r="4.5" fill="#fff"/>
        <line x1="316" y1="233" x2="316" y2="235.5"/><line x1="316" y1="250.5" x2="316" y2="253"/>
        <line x1="306" y1="243" x2="308.5" y2="243"/><line x1="323.5" y1="243" x2="326" y2="243"/>
        <line x1="309" y1="236" x2="310.7" y2="237.7"/><line x1="321.3" y1="248.3" x2="323" y2="250"/>
        <line x1="323" y1="236" x2="321.3" y2="237.7"/><line x1="310.7" y1="248.3" x2="309" y2="250"/>
      </g>
    </g>

    <text class="brand-name" x="38" y="104" font-size="22">Korunelle</text>

    <text class="headline" x="33" y="186" font-size="64"><tspan class="hl-green">AM</tspan> <tspan class="hl-teal">FORMEL</tspan></text>

    <g class="benefits">
      <g><circle cx="44" cy="219" r="8" fill="var(--green)"/><polyline points="40,219 43,222 48.5,215.5" fill="none" stroke="#fff" stroke-width="1.8"/>
        <text class="body-text" x="59" y="223" font-size="10.5">Unterstützt die Tagesenergie</text></g>
      <g><circle cx="44" cy="249" r="8" fill="var(--green)"/><polyline points="40,249 43,252 48.5,245.5" fill="none" stroke="#fff" stroke-width="1.8"/>
        <text class="body-text" x="59" y="253" font-size="10.5">Mitochondriale Aktivierung</text></g>
      <g><circle cx="44" cy="279" r="8" fill="var(--green)"/><polyline points="40,279 43,282 48.5,275.5" fill="none" stroke="#fff" stroke-width="1.8"/>
        <text class="body-text" x="59" y="283" font-size="10.5">Hilft, biologische Rhythmen zu regulieren</text></g>
    </g>

    <g class="quality-badge">
      <rect x="34" y="316" width="142" height="46" rx="12" fill="none" stroke="var(--green)" stroke-width="1.4"/>
      <text class="percent" x="44" y="350" font-size="29">100%</text>
      <text class="body-text" x="108" y="337" font-size="7">Sicher &amp;</text>
      <text class="body-text" x="108" y="346" font-size="7">qualitätsgeprüft</text>
    </g>

    <g class="capsule-count" text-anchor="middle">
      <text class="count" x="316" y="332" font-size="58">30</text>
      <text class="body-text strong" x="316" y="350" font-size="10.5" fill="var(--teal)">KAPSELN</text>
    </g>

    <g class="footer">
      <rect x="0" y="420" width="383" height="68" fill="var(--teal)"/>
      <path d="M160 488 L190 410 Q198 386 224 386 H383 V488 Z" fill="url(#am-panel)"/>
      <text class="white-text" x="32" y="457" font-size="11.5">korunelle.com</text>
      <text class="white-text strong" x="213" y="421" font-size="10">Morgen-Nährstoffkomplex</text>
      <text class="white-text" x="213" y="437" font-size="6.6">Formuliert zur Unterstützung der</text>
      <text class="white-text" x="213" y="447" font-size="6.6">zellulären Energieproduktion und zur</text>
      <text class="white-text" x="213" y="457" font-size="6.6">Förderung optimaler Morgenenergie.</text>
    </g>
  </svg>

  <!-- PM Formel tin label -->
  <svg class="label label--pm" viewBox="0 0 383 488" aria-labelledby="pm-title">
    <title id="pm-title">Korunelle PM Formel Etikett</title>
    <defs>
      <linearGradient id="pm-pill" x1="0" y1="0" x2="0" y2="1">
        <stop offset="0" stop-color="#d9ec9a"/>
        <stop offset="1" stop-color="#9cc23a"/>
      </linearGradient>
      <linearGradient id="pm-panel" x1="0" y1="0" x2="1" y2="1">
        <stop offset="0" stop-color="#b5d55a"/>
        <stop offset="1" stop-color="#97bf33"/>
      </linearGradient>
    </defs>

    <g class="time-pill">
      <path d="M296 0 H336 V250 A20 20 0 0 1 296 250 Z" fill="url(#pm-pill)"/>
      <text class="white-text" font-size="13" transform="translate(321 196) rotate(-90)">Abends einnehmen</text>
      <g class="icon-moon" fill="#fff">
        <path d="M319 235 A8.5 8.5 0 1 0 325 248 A6.5 6.5 0 1 1 319 235 Z"/>
        <circle cx="324" cy="237" r="1.3"/>
      </g>
    </g>

    <text class="brand-name" x="38" y="104" font-size="22">Korunelle</text>

    <text class="headline" x="33" y="186" font-size="64"><tspan class="hl-green">PM</tspan> <tspan class="hl-teal">FORMEL</tspan></text>

    <g class="benefits">
      <g><circle cx="44" cy="219" r="8" fill="var(--green)"/><polyline points="40,219 43,222 48.5,215.5" fill="none" stroke="#fff" stroke-width="1.8"/>
        <text class="body-text" x="59" y="223" font-size="10.5">Unterstützt die nächtliche Regeneration</text></g>
      <g><circle cx="44" cy="249" r="8" fill="var(--green)"/><polyline points="40,249 43,252 48.5,245.5" fill="none" stroke="#fff" stroke-width="1.8"/>
        <text class="body-text" x="59" y="253" font-size="10.5">Reduziert oxidativen Stress</text></g>
      <g><circle cx="44" cy="279" r="8" fill="var(--green)"/><polyline points="40,279 43,282 48.5,275.5" fill="none" stroke="#fff" stroke-width="1.8"/>
        <text class="body-text" x="59" y="283" font-size="10.5">Fördert tiefe Erholung</text></g>
    </g>

    <g class="quality-badge">
      <rect x="34" y="316" width="142" height="46" rx="12" fill="none" stroke="var(--green)" stroke-width="1.4"/>
      <text class="percent" x="44" y="350" font-size="29">100%</text>
      <text class="body-text" x="108" y="337" font-size="7">Sicher &amp;</text>
      <text class="body-text" x="108" y="346" font-size="7">qualitätsgeprüft</text>
    </g>

    <g class="capsule-count" text-anchor="middle">
      <text class="count" x="316" y="332" font-size="58">30</text>
      <text class="body-text strong" x="316" y="350" font-size="10.5" fill="var(--teal)">KAPSELN</text>
    </g>

    <g class="footer">
      <rect x="0" y="420" width="383" height="68" fill="var(--teal)"/>
      <path d="M160 488 L190 410 Q198 386 224 386 H383 V488 Z" fill="url(#pm-panel)"/>
      <text class="white-text" x="32" y="457" font-size="11.5">korunelle.com</text>
      <text class="white-text strong" x="213" y="421" font-size="10">Abend-Nährstoffkomplex</text>
      <text class="white-text" x="213" y="437" font-size="6.6">Formuliert zur Unterstützung tiefer</text>
      <text class="white-text" x="213" y="447" font-size="6.6">nächtlicher Reparaturprozesse und zur</text>
      <text class="white-text" x="213" y="457" font-size="6.6">Förderung gesunder Zellregeneration.</text>
    </g>
  </svg>

  <!-- Longevity test tin lid -->
  <svg class="label label--test" viewBox="0 0 403 595" aria-labelledby="test-title">
    <title id="test-title">Korunelle Langlebigkeits Diagnosetest Deckel</title>
    <defs>
      <linearGradient id="dose-bar" x1="0" y1="0" x2="1" y2="0">
        <stop offset="0" stop-color="#e4f1b6"/>
        <stop offset="0.35" stop-color="#b8d75e"/>
        <stop offset="1" stop-color="#9cc23a"/>
      </linearGradient>
    </defs>

    <text class="brand-name" x="46" y="160" font-size="22">Korunelle</text>

    <text class="headline hl-green" x="43" y="244" font-size="53">LANGLEBIGKEITS</text>
    <text class="headline hl-teal" x="43" y="298" font-size="53">DIAGNOSETEST</text>

    <text class="muted-text" x="46" y="330" font-size="11">Messen, was wirklich zählt. Verstehen Sie Ihr</text>
    <text class="muted-text" x="46" y="343" font-size="11">biologisches Alter.</text>

    <g class="dose-row">
      <path d="M0 378 H300 A22.5 22.5 0 0 1 300 423 H0 Z" fill="url(#dose-bar)"/>
      <text class="dose-count" x="43" y="419" font-size="52">1X</text>
      <text class="white-text" x="104" y="405" font-size="12.5">Morning Supplement-Dose</text>
      <g class="icon-sun" stroke="#fff" stroke-width="1.6" stroke-linecap="round">
        <circle cx="296" cy="400.5" r="4.5" fill="#fff"/>
        <line x1="296" y1="390.5" x2="296" y2="393"/><line x1="296" y1="408" x2="296" y2="410.5"/>
        <line x1="286" y1="400.5" x2="288.5" y2="400.5"/><line x1="303.5" y1="400.5" x2="306" y2="400.5"/>
        <line x1="289" y1="393.5" x2="290.7" y2="395.2"/><line x1="301.3" y1="405.8" x2="303" y2="407.5"/>
        <line x1="303" y1="393.5" x2="301.3" y2="395.2"/><line x1="290.7" y1="405.8" x2="289" y2="407.5"/>
      </g>
    </g>

    <g class="dose-row">
      <path d="M0 435 H300 A22.5 22.5 0 0 1 300 480 H0 Z" fill="url(#dose-bar)"/>
      <text class="dose-count" x="43" y="476" font-size="52">1X</text>
      <text class="white-text" x="104" y="462" font-size="12.5">Evening Supplement-Dose</text>
      <g class="icon-moon" fill="#fff">
        <path d="M298 449 A8.5 8.5 0 1 0 304 462 A6.5 6.5 0 1 1 298 449 Z"/>
        <circle cx="303" cy="451" r="1.3"/>
      </g>
    </g>

    <g class="footer">
      <rect x="0" y="552" width="403" height="43" fill="var(--teal)"/>
      <text class="white-text" x="201.5" y="578" font-size="11" text-anchor="middle">korunelle.com</text>
    </g>
  </svg>

</main>
</body>
</html>
```